Law Firm Business Card

This is a business card for a law firm that serves US military and veterans.

The card must have ONLY the following (we want an uncluttered look):

- Company logo (PNG, GIF, JPEG copies uploaded)
- A tagline reading: "a law firm for service members and veterans"
- My name and title: "Martin Okello" and "Attorney"
- My email: "martin.okello@harborlinecounsel.com"
- My number: "855-FILE-NOW (345-3669)"

We are looking for a clean, simple layout with only the above information, likely printed on a bright white cotton stock. The font of our logo is DIN 1451, and the font used on our website is Helvetica Neue. The color of our logo is #336699, and we probably want the tagline in that color also, and my contact information in a dark grey. Please review our website at www.harborlinecounsel.com to ensure your card design complements our website style.

Thanks and we look forward to seeing your submissions.

A few notes:

- Two-sided submissions are ok
- Please don't add graphics (scales of justice, judges hammer, etc)

```html
<!DOCTYPE html>
<html lang="en">
<head>
<meta charset="utf-8">
<title>Harborline Counsel – Business Card</title>
<link rel="stylesheet" href="https://fonts.googleapis.com/css2?family=Open+Sans:wght@400;700&display=swap">
<style>
  :root {
    --backdrop: #0c0c0c;
    --card-white: #ffffff;
    --brand-blue: #2768bf;
    --ink: #141414;
  }
  * { margin: 0; padding: 0; box-sizing: border-box; }
  html, body {
    width: 1200px;
    height: 1000px;
    overflow: hidden;
    background: var(--backdrop);
    font-family: "Open Sans", Helvetica, Arial, sans-serif;
  }
  .canvas {
    position: relative;
    width: 1200px;
    height: 1000px;
  }
  .business-card {
    position: absolute;
    left: 173px;
    top: 250px;
    width: 854px;
    height: 501px;
    background: var(--card-white);
    box-shadow: 0 12px 30px rgba(0, 0, 0, 0.6);
    overflow: hidden;
  }
  .edge-stripe {
    position: absolute;
    left: 0;
    width: 100%;
    height: 14px;
    background: var(--brand-blue);
  }
  .edge-stripe--top { top: 0; }
  .edge-stripe--bottom { bottom: 0; }

  .holder-name,
  .holder-title,
  .contact-email,
  .contact-phone {
    position: absolute;
    color: var(--ink);
    font-size: 18px;
    font-weight: 400;
    letter-spacing: 0.1px;
  }
  .holder-name { left: 34px; top: 39px; }
  .holder-title { right: 34px; top: 39px; }
  .contact-email { left: 45px; top: 436px; }
  .contact-phone { right: 45px; top: 436px; }

  .brand-band {
    position: absolute;
    left: 0;
    top: 135px;
    width: 100%;
    height: 205px;
    background: var(--brand-blue);
    display: flex;
    flex-direction: column;
    align-items: center;
    justify-content: center;
    color: var(--card-white);
    font-weight: 700;
    text-transform: uppercase;
    line-height: 1;
  }
  .brand-name__main {
    font-size: 58px;
    letter-spacing: 0.5px;
  }
  .brand-name__sub {
    margin-top: 10px;
    font-size: 32px;
    letter-spacing: 6px;
  }

  .tagline {
    position: absolute;
    left: 0;
    top: 349px;
    width: 100%;
    text-align: center;
    color: var(--brand-blue);
    font-size: 19px;
    font-weight: 400;
  }
</style>
</head>
<body>
  <main class="canvas">
    <article class="business-card">
      <div class="edge-stripe edge-stripe--top"></div>

      <p class="holder-name">MARTIN OKELLO</p>
      <p class="holder-title">ATTORNEY</p>

      <div class="brand-band" aria-label="Harborline Counsel">
        <span class="brand-name__main">Harborline</span>
        <span class="brand-name__sub">Counsel</span>
      </div>

      <p class="tagline">a law firm for service members and veterans</p>

      <p class="contact-email">martin.okello@harborlinecounsel.com</p>
      <p class="contact-phone">855-FILE-NOW (345-3669)</p>

      <div class="edge-stripe edge-stripe--bottom"></div>
    </article>
  </main>
</body>
</html>
```